Landing page for selling a web application used by archeologists

We are selling a web program that professional archeologists use. This program is developed and designed already. But we are now building another website for presenting this web program.
I have uploaded a pdf file that shows the mockup of the future web page. You will also find a folder containing the photos used in the mockup. You can use your own photos for the ones named with "(can be changed)".
There is another folder called "otherPhoto". You can use them if you want to do background or ambiance...
We expect a really clean, serious, and professional design.

You will see in the mockup that there is a first part (main header) followed by 6 subparts presenting the different aspect of the web app. It finishes with the last part presenting ourselves and inviting to test the program.

Here are some links to website designs that go in the direction of what we want.
https://morvani.quillbarrow.com/startup/#home
https://www.tarnpixel-wp. com/mobileapp-landing/
https://en.brovalent.com/
https://assets.plorvik.com/en/klyma-saas-software-landing-html5-page-template-RT4PW9/preview

Don't hesitate to contact me if you need more explanations.
As requested by a designer, I also added 2 print screen of the app that we are selling.
Updates

Feel free to use your own photos for background images for example...

Target Market(s)

Professional archaeologists

Industry/Entity Type

Archeology

Number of Pages Required

1 page

Colors
0054AA
0677BA
7BADD7
CADEEF
E8F1F8
0094D4
00A9DD
6FCCEA
C7EBF8
E9F6FB
FFC000
F8CF3A
FAE287
FDF2CF
FEFAEE

Requirements
Must have
• A professional look that says that our company is large and serious

```html
<!DOCTYPE html>
<html lang="en">
<head>
<meta charset="utf-8">
<title>Sondalis — Technology Serving Archaeology</title>
<link rel="stylesheet" href="https://fonts.googleapis.com/css2?family=Roboto:wght@300;400;700&family=Montserrat:wght@400;500;600;700&display=swap">
<style>
:root{
  --blue:#2a45c1;
  --blue-soft:#7b95e0;
  --ink:#1f1f24;
  --text:#4a4a52;
  --muted:#7a7a82;
  --white:#ffffff;
  --footer:#2b2b2f;
}
*{margin:0;padding:0;box-sizing:border-box}
html,body{width:1200px;height:4785px;overflow:hidden}
body{position:relative;font-family:"Montserrat",sans-serif;color:var(--text);background:var(--white)}
.abs{position:absolute}
.wordmark{font-family:"Roboto",sans-serif;font-weight:700}
.title{font-family:"Roboto",sans-serif;font-weight:300;font-size:38px;color:var(--ink);line-height:1}
.title b{font-weight:700}
.copy{font-size:15px;line-height:26px;color:var(--muted)}
.lead{font-size:15px;line-height:26px;color:var(--ink);font-weight:500}
.btn{position:absolute;display:flex;align-items:center;justify-content:center;border-radius:24px;font-size:14px;font-weight:700;letter-spacing:.4px;text-transform:uppercase;background:var(--blue);color:var(--white);box-shadow:0 6px 14px rgba(42,69,193,.25)}
.btn.inv{background:var(--white);color:var(--blue);box-shadow:0 6px 14px rgba(0,0,0,.15)}
.img{position:absolute;border-radius:6px}

.hero{position:absolute;left:0;top:0;width:1200px;height:557px;background:linear-gradient(180deg,#f4f4f6 0%,#e9eaee 100%)}
.logo{position:absolute;left:111px;top:34px;font-size:36px;color:var(--ink)}
.nav{position:absolute;left:637px;top:44px;display:flex;gap:32px;font-size:15px;font-weight:500;color:var(--ink)}
.login{left:960px;top:28px;width:127px;height:52px;gap:8px}
.hero h1{position:absolute;left:111px;top:212px;font-family:"Roboto",sans-serif;font-size:38px;line-height:46px;color:var(--ink);font-weight:700}
.hero h1 span{display:block;font-weight:300}
.hero p{position:absolute;left:111px;top:318px;width:400px;font-size:16px;line-height:26px;color:var(--ink)}
.hero p b{font-weight:700}

.band-blue{position:absolute;left:0;width:1200px;background:var(--blue)}
.center{position:absolute;left:0;width:1200px;text-align:center}
.section-gray{position:absolute;left:0;top:1841px;width:1200px;height:472px;background:linear-gradient(120deg,#f3f3f5,#e8e9ec)}

.card{position:absolute;top:3974px;width:309px;height:380px;background:var(--white);box-shadow:0 8px 26px rgba(0,0,0,.1);text-align:center;padding:0 18px}
.card svg{margin-top:30px}
.card h3{margin-top:26px;font-size:18px;line-height:26px;font-weight:700;color:var(--ink);text-transform:uppercase}
.card p{margin-top:22px;font-size:12.5px;line-height:23px;color:var(--muted)}

.footer{position:absolute;left:0;top:4576px;width:1200px;height:209px;background:var(--footer);color:var(--white)}
.footnav{position:absolute;left:0;top:106px;width:1200px;display:flex;justify-content:center;gap:24px;font-size:16px;font-weight:500}
.footnav i{font-style:normal;opacity:.8}
.rule{position:absolute;left:111px;top:144px;width:978px;height:1px;background:rgba(255,255,255,.2)}
.social{position:absolute;top:162px;width:36px;height:36px;border-radius:50%;background:var(--white)}
</style>
</head>
<body>

<section class="hero">
  <div class="logo wordmark">Sondalis</div>
  <nav class="nav"><span>SOLUTION</span><span>PRICE</span><span>CONTACT</span></nav>
  <a class="btn login">
    <svg width="16" height="16" viewBox="0 0 16 16"><circle cx="8" cy="8" r="7" fill="none" stroke="#fff" stroke-width="1.6"/><circle cx="8" cy="6.5" r="2.3" fill="#fff"/><path d="M3.8 12.6c1-1.8 2.4-2.6 4.2-2.6s3.2.8 4.2 2.6" fill="#fff"/></svg>
    Login
  </a>
  <h1>Technology Serving<span>Sondalis</span></h1>
  <p><b>Sondalis</b> the solution to input, analyse and promote the archaeological heritage</p>
  <a class="btn" style="left:111px;top:392px;width:155px;height:50px">Get started</a>
  <div class="img" role="img" aria-label="Two desktop monitors showing the application map and record screens" style="left:492px;top:139px;width:595px;height:381px;background:linear-gradient(135deg,#cfd2d8,#9ea3ab 55%,#e4e6ea);border-radius:10px"></div>
</section>

<section class="band-blue" style="top:557px;height:528px">
  <svg class="abs" style="left:0;top:0" width="1200" height="120" viewBox="0 0 1200 120"><path d="M0 0 Q600 224 1200 0 Z" fill="#ebecef"/><path d="M0 4 Q600 228 1200 4" fill="none" stroke="#7b95e0" stroke-width="3" opacity=".6"/></svg>
  <div class="center title" style="top:166px;color:#fff"><b>Sonda</b>Entry</div>
  <p class="center" style="top:222px;font-size:15px;color:#fff">Capture of archaeological information. How to make more, faster, with the same amount of resources ?</p>
  <p class="center" style="top:256px;font-size:15px;font-weight:500;color:#fff">Sondalis as force multiplier</p>
  <a class="btn inv" style="left:518px;top:305px;width:164px;height:47px">More details</a>
</section>
<div class="img" role="img" aria-label="Desktop screen and tablet displaying the data entry tables" style="left:269px;top:944px;width:660px;height:342px;background:linear-gradient(160deg,#2b2b2f,#54575e 40%,#dfe2e8 42%,#f4f5f7)"></div>

<section>
  <div class="img" role="img" aria-label="Statistical charts: histograms, scatter plot and heat map dendrogram" style="left:111px;top:1341px;width:419px;height:415px;background:linear-gradient(135deg,#e6ebf5,#f7f7f9 50%,#f5dcb0)"></div>
  <div class="abs title" style="left:598px;top:1405px"><b>Sonda</b>Analysis</div>
  <p class="abs copy" style="left:598px;top:1470px;width:490px">Analysis of archaeological information. How to detect hidden relationships, make sense of the information and preserve the big picture?</p>
  <p class="abs lead" style="left:598px;top:1559px;width:490px;text-align:justify;text-align-last:left">Sondalis as an intuitive solution to complex analysis problems</p>
  <a class="btn" style="left:598px;top:1646px;width:164px;height:47px">More details</a>
</section>

<section class="section-gray">
  <div class="abs title" style="left:184px;top:88px"><b>Sonda</b>Publication</div>
  <p class="abs copy" style="left:184px;top:154px;width:490px;text-align:justify;text-align-last:left">Publication of archaeological information. How to publish in a scientifc format and fnd the information scattered among multiple</p>
  <p class="abs lead" style="left:184px;top:244px;width:420px">Sondalis as a tool for publishing and searching information</p>
  <a class="btn" style="left:184px;top:331px;width:164px;height:47px">More details</a>
  <div class="img" role="img" aria-label="Tablet showing a published excavation report page" style="left:756px;top:62px;width:249px;height:349px;background:linear-gradient(180deg,#7a5a44 0%,#9a7a60 18%,#fafafa 19%,#e8e8ea);border:8px solid #222;border-radius:14px"></div>
</section>

<section class="band-blue" style="top:2313px;height:472px">
  <div class="img" role="img" aria-label="Photograph of a lakeside medieval castle under blue sky" style="left:111px;top:56px;width:445px;height:359px;border-radius:0;background:linear-gradient(180deg,#8fb6e2 0%,#c6d8ee 40%,#9d948a 60%,#6f7a82 100%)"></div>
  <div class="abs title" style="left:598px;top:101px;color:#fff"><b>Sonda</b>View</div>
  <p class="abs" style="left:598px;top:166px;width:490px;font-size:15px;line-height:26px;color:#fff">Promotion of the archaeological heritage. How to render the archaeological heritage accessible to the general public, as well as to the educational and tourist sectors?</p>
  <p class="abs" style="left:598px;top:256px;font-size:15px;font-weight:500;color:#fff">Sondalis as a mobilizing and unifying power</p>
  <a class="btn inv" style="left:598px;top:320px;width:164px;height:47px">More details</a>
</section>

<section>
  <div class="abs title" style="left:111px;top:2882px"><b>Sonda</b>Forum</div>
  <p class="abs copy" style="left:111px;top:2947px;width:490px">Staying in touch with the community. How to connect among specialists and exchange ideas across borders and languages ?</p>
  <p class="abs lead" style="left:111px;top:3017px;width:490px;text-align:justify;text-align-last:left">SondaForum as a solution for multilingual specialist networking</p>
  <a class="btn" style="left:111px;top:3103px;width:164px;height:48px">More details</a>
  <div class="img" role="img" aria-label="Illustration of a network of connected specialists" style="left:632px;top:2861px;width:483px;height:316px;background:radial-gradient(ellipse at center,#e4e8f7 0%,#ffffff 70%)"></div>
</section>

<section class="abs" style="left:0;top:3248px;width:1200px;height:474px">
  <div class="abs" role="img" aria-label="Photograph of stacked archive files and paper folders" style="left:0;top:0;width:1200px;height:474px;background:linear-gradient(100deg,#6d6a66 0%,#c9c3b8 30%,#8c8780 55%,#d6d5d3 100%)"></div>
  <div class="abs" style="left:598px;top:82px;width:489px;height:340px;background:rgba(255,255,255,.93)"></div>
  <div class="abs title" style="left:622px;top:112px"><b>Sonda</b>Archive</div>
  <p class="abs copy" style="left:622px;top:176px;width:450px">Retrieval of information How to fnd information quickly within archives in various formats (pdf, xls, doc, etc.) ?</p>
  <p class="abs lead" style="left:622px;top:247px">Sondalis as a solution for dispersed information</p>
  <a class="btn" style="left:622px;top:310px;width:164px;height:48px">More details</a>
</section>

<section>
  <div class="center title wordmark" style="top:3798px;font-weight:700">Sondalis</div>
  <p class="center copy" style="top:3855px;left:120px;width:960px">Innovative, reliable, at the cutting edge of technology. Founded by a Swiss team of computer engineers and statistical analysts, Sondalis places innovation at the service of success. Its vocation: to ofer the latest computer tools to the world of archaeology in order to facilitate and promote the work of archaeologists</p>

  <div class="card" style="left:111px">
    <svg width="72" height="72" viewBox="0 0 72 72"><circle cx="36" cy="36" r="30" fill="none" stroke="#2a45c1" stroke-width="5"/><path d="M22 37l10 10 19-21" fill="none" stroke="#2a45c1" stroke-width="6" stroke-linecap="round" stroke-linejoin="round"/></svg>
    <h3>The expertise &amp; security of a swiss company</h3>
    <p>We bring together the most advanced technical engineering skills to deploy the right solutions for the most demanding problems. Big data input and processing, scalability, statistic analysis, deep learning, machine learning are our daily routine.</p>
  </div>
  <div class="card" style="left:446px">
    <svg width="72" height="72" viewBox="0 0 72 72"><path d="M8 38L36 10h24v24L32 62z" fill="none" stroke="#2a45c1" stroke-width="5" stroke-linejoin="round"/><circle cx="48" cy="22" r="5" fill="#2a45c1"/></svg>
    <h3>Afordable<br>prices</h3>
    <p>Budgets in archaeology are often limited. Reaching a large number of users allows advanced technological services that are usually very expensive to be ofered at very low prices.</p>
  </div>
  <div class="card" style="left:780px">
    <svg width="72" height="72" viewBox="0 0 72 72"><path d="M60 36a24 24 0 1 1-7-17" fill="none" stroke="#2a45c1" stroke-width="6" stroke-linecap="round"/><path d="M56 8v14H42" fill="none" stroke="#2a45c1" stroke-width="6" stroke-linecap="round" stroke-linejoin="round"/></svg>
    <h3>Ongoing<br>developments</h3>
    <p>Accompanied by professional archaeologists, we are continually shaping Sondalis to meet their precise needs and expectations. We are always listening to new development proposals in order to solve the problems that archaeologists from all countries have in common.</p>
  </div>

  <p class="center" style="top:4406px;font-size:21px;font-weight:500;color:var(--ink)">Get now a free 3-month trial of Sondalis</p>
  <a class="btn" style="left:522px;top:4454px;width:156px;height:48px">Contact us</a>
</section>

<footer class="footer">
  <div class="center wordmark" style="top:42px;font-size:38px;color:#fff">Sondalis</div>
  <nav class="footnav"><span>HOME</span><i>|</i><span>SOLUTION</span><i>|</i><span>PRICE</span><i>|</i><span>CONTACT US</span><i>|</i><span>PRIVACY</span><i>|</i><span>TERMS OF USE</span></nav>
  <div class="rule"></div>
  <p class="center" style="top:172px;font-size:13px">© 2022 <b>Sondalis</b> &nbsp;|&nbsp; All Rights Reserved</p>
  <span class="social" style="left:969px"></span>
  <span class="social" style="left:1011px"></span>
  <span class="social" style="left:1052px"></span>
</footer>

</body>
</html>
```